Wordpress Design for Financial Trading Software

Our Software QuantoMesh allows clients to program their trading strategy and use it to trade automatically on stock markets. For further details please visit our preliminary / draft web page: http://www.quantomesh-example.ch/wordpress.
We would like the Web Page to represent the following values:
- Innovative
- High Tech
- High Quality
- Professional
- Sophisticated
- State-of-the-art
- Modern
- Versatile
We need a Design based on a PSD file for the Main Page containing the following:
Header:
- Logo + optional Image / Graphic / Slogan / Quote
- Menu Bar with drop-down for Sub-Menus
- Search Box
Full Width Featured Content Area
- Main Description of the Product (with read-more Link + optional Image / Graphic)
Smaller Featured Content Areas:
- Product Features (with read-more Link + optional Icon)
- Documentation and Demo (with read-more Link + optional Icon)
- Professional Services (with read-more Link + optional Icon)
- Training (with read-more Link + optional Icon)
Latest News:
- 3-5 latest News + option Image / Grafic
Testimonial:
- 1 Customer Testimonial with Photo
Footer:
- Copyright and "all rights reserved" Notice
- Privacy Policy
- Contact Info: Address, Phone Number and Email
- Link to Site-Map
- Social Media Connectors (Chatterwall, CareerWeave, RSS Feed & Email)
Guidelines for Style/Theme:
- Well structured, Lean, Easy-to-use Page
- Use of existing Logo
- Sans-Serif Fonts
- Colors matching our Logo (not too many Colors)
- Main Focus: Desktop-Computers.
- However: Page should be readable on mobile Devices also
- Please show one element of the navigation bar in selected state with drop-down
- After the contest we will work with the Designer on the other Pages
- We will need a PSD File, so that we can organize the actual coding of the Wordpress Page / Theme
- If images / photos are used, they have to be royalty-free.
Example Pages that we like:
http://www.brindlecove.example/
http://www.hqz.example/
http://www.mockturn.example/
http://www.marketloft.example/
http://www.nimbravault.example/
http://www.shelfgrid.example/
http://www.pme-werkplatz.example.ch/
https://www.o-volving.example/
http://www.dealharbor.example/
https://sketchrally.example/web-design/contests/green-power-ventures-exchange-portal-website-design-402817/entries/38172640
https://sketchrally.example/web-design/contests/website-design-wanted-halvex-holdings-57210/entries/6431872
http://files.artpooling.example/design_img/482917/37650/37650_2948301_482917_image.jpg
WordPress Plugins currently in use:
- Quick Safe Inquiry Box
- Glowpane Album
- PinTrail Simple Terrain Charts
Reason: A few Designers let us know, that they need more time to work on their Designs. We are in no rush and would like to see as many good Designs as possible!
Target Market(s)
Investment Banks and Hedge Funds
Industry/Entity Type
Trade

```html
<!DOCTYPE html>
<html lang="en">
<head>
<meta charset="utf-8">
<title>QuantoMesh — Algorithmic Trading Platform</title>
<link rel="stylesheet" href="https://fonts.googleapis.com/css2?family=Roboto+Condensed:wght@400;700&family=Arimo:wght@400;700&display=swap">
<style>
:root{
  --ink:#2b2b2b;
  --body:#555b61;
  --navy:#1f3d5e;
  --link:#23527c;
  --gold:#d8b86a;
  --gold-light:#ecd896;
  --gold-dark:#b99442;
  --slate:#3f4d59;
  --hero-a:#5d7585;
  --hero-b:#33444f;
  --btn-blue:#2c6ea6;
  --btn-blue-dark:#1f5283;
  --panel:#f1f1f1;
  --rule:#e2e2e2;
  --footer:#3a4249;
  --footer-bar:#2c3237;
  --footer-text:#c7ccd0;
  --white:#ffffff;
}
*{box-sizing:border-box;margin:0;padding:0}
html,body{width:1200px;height:3118px;overflow:hidden}
body{position:relative;background:var(--white);font-family:"Arimo",Arial,sans-serif;color:var(--body);font-size:13px;line-height:1.55}
.abs{position:absolute}
h2{font-family:"Roboto Condensed",Arial,sans-serif;font-weight:700;color:var(--ink);font-size:27px}

/* header */
.site-header{left:0;top:0;width:1200px;height:190px;background:var(--white)}
.util{right:60px;top:26px;display:flex;align-items:center;gap:18px;font-size:13px;color:var(--ink)}
.util .sep{color:#999}
.search{width:210px;height:32px;border:1px solid #ddd;background:#fff;display:flex;align-items:center;justify-content:space-between;padding:0 8px;font-size:11px;color:#333;letter-spacing:.3px}
.brand{left:36px;top:80px;display:flex;align-items:center;gap:12px}
.brand .mark{width:34px;height:34px;background:var(--gold)}
.brand .name{font-family:"Roboto Condensed",Arial,sans-serif;font-weight:700;font-size:38px;color:var(--slate);line-height:1}
.brand-tag{left:84px;top:122px;font-size:8px;letter-spacing:1px;color:var(--slate);text-transform:uppercase}
.nav{left:600px;top:120px;display:flex;font-size:13px;color:var(--ink);text-transform:uppercase}
.nav a{display:block;padding:0 22px;height:34px;line-height:34px;color:inherit;text-decoration:none}
.nav a.active{background:var(--slate);color:#fff}
.dropdown{left:810px;top:170px;width:152px;background:#fff;box-shadow:0 2px 6px rgba(0,0,0,.25)}
.dropdown a{display:block;height:34px;line-height:34px;padding-left:16px;font-size:13px;color:var(--ink);text-decoration:none;background:linear-gradient(var(--gold-light),var(--gold));border-bottom:1px solid var(--gold-dark)}
.dropdown a.current{background:var(--slate);color:#fff}

/* hero */
.hero{left:0;top:190px;width:1200px;height:510px;background:radial-gradient(ellipse at 55% 45%,var(--hero-a),var(--hero-b) 75%)}
.hero h1{position:absolute;left:66px;top:60px;font-family:"Roboto Condensed",Arial,sans-serif;font-weight:700;font-size:30px;color:#fff}
.hero p{position:absolute;left:66px;top:158px;width:395px;color:#eef2f4;font-size:13px;line-height:1.6}
.hero .btn{position:absolute;top:383px;width:112px;height:36px;line-height:36px;text-align:center;font-size:14px;border-radius:3px}
.btn-buy{left:66px;background:linear-gradient(#b9d4e8,#7fa8c8);color:#1f3d5e}
.btn-demo{left:228px;background:linear-gradient(#f2dc9c,var(--gold));color:#3a2c10}
.hero-art{left:560px;top:30px;width:610px;height:440px;border-radius:6px;background:radial-gradient(circle at 60% 40%,#d9e6f2,#7aa0c4 45%,rgba(60,80,100,0) 75%)}
.dots{right:42px;top:478px;display:flex;gap:8px}
.dots i{width:10px;height:10px;border-radius:50%;background:#fff;opacity:.6}
.dots i.on{opacity:1}

/* why */
.why h2{position:absolute;left:33px;top:755px}
.why-text{left:33px;top:800px;width:540px;font-size:13px;line-height:1.6}
.benefits{left:33px;top:1022px;list-style:none}
.benefits li{display:flex;align-items:center;gap:20px;height:53px;font-size:13px;color:var(--ink)}
.tablet{left:600px;top:765px;width:565px;height:380px;border-radius:22px;background:#1b1d1f;padding:26px 30px}
.tablet .screen{width:100%;height:100%;background:linear-gradient(135deg,#f4f8f4,#dfeee2 60%,#c9dccd)}
.btn-download{left:797px;top:1180px;width:190px;height:52px;line-height:52px;text-align:center;background:linear-gradient(var(--btn-blue),var(--btn-blue-dark));color:#fff;font-size:17px;border-radius:3px}

.rule{left:0;width:1200px;height:1px;background:var(--rule)}

/* services */
.services h2{position:absolute;left:33px;top:1345px}
.service{top:1432px;width:210px;text-align:center}
.service .disc{margin:0 auto;width:172px;height:172px;border-radius:50%;background:#fff;border:3px solid #ececec;display:flex;align-items:center;justify-content:center}
.service .disc.on{background:radial-gradient(circle,var(--gold-light),var(--gold) 70%);border-color:#f4ecd2}
.service h3{margin-top:12px;font-family:"Roboto Condensed",Arial,sans-serif;font-weight:700;font-size:18px;color:var(--navy);line-height:1.2}
.service-summary{left:33px;top:1672px;width:1137px;height:160px;background:var(--panel);padding:16px 14px;font-size:12.5px;line-height:1.75}
.btn-dark{background:var(--slate);color:#fff;font-size:13px;text-align:center;border-radius:3px}

/* news & testimonials */
.col-rule{left:602px;top:1912px;width:1px;height:760px;background:var(--rule)}
.news-head{left:33px;top:1980px}
.testi-head{left:640px;top:1980px}
.arrows{left:1080px;top:1984px;display:flex;gap:12px}
.arrows i{width:28px;height:28px;border-radius:50%;border:1px solid #ddd}
.news-item{left:33px;width:540px;height:150px}
.news-item .thumb{position:absolute;left:0;top:0;width:118px;height:82px;background:linear-gradient(135deg,#eef3f6,#9fc2da 60%,#6f9d4f)}
.news-item h4{position:absolute;left:140px;top:0;font-weight:400;font-size:18px;color:var(--link);line-height:1.2}
.news-item time{position:absolute;left:140px;top:26px;font-size:11px;color:#999}
.news-item p{position:absolute;left:140px;top:46px;width:400px;font-size:13px;line-height:1.5}
.news-item .more{position:absolute;right:40px;top:118px;font-size:12px;color:var(--ink);font-weight:700}
.testimonial{left:705px;width:465px;height:170px}
.testimonial blockquote{font-size:13px;line-height:1.55}
.testimonial cite{position:absolute;left:105px;top:113px;font-style:normal;font-weight:700;font-size:11.5px;color:var(--navy)}
.testimonial .photo{position:absolute;right:0;top:98px;width:88px;height:62px;border:3px solid #eee;background:linear-gradient(#f6e3cf,#d8b59a)}

/* footer */
.site-footer{left:0;top:2745px;width:1200px;height:373px;background:var(--footer);color:var(--footer-text)}
.site-footer h5{position:absolute;top:22px;font-family:"Roboto Condensed",Arial,sans-serif;font-weight:400;font-size:18px;letter-spacing:.5px;color:var(--gold);text-transform:uppercase}
.quick{position:absolute;left:33px;top:75px;list-style:none;font-size:12px;text-transform:uppercase;line-height:24px}
.contact-row{position:absolute;left:445px;display:flex;gap:22px;font-size:12.5px;line-height:1.5}
.news-label{position:absolute;left:858px;top:70px;font-family:"Roboto Condensed",Arial,sans-serif;font-size:17px;color:var(--gold)}
.signup{position:absolute;left:858px;top:115px;width:317px;height:42px;background:#fff;border-radius:4px;display:flex;align-items:center;justify-content:space-between;padding:0 6px 0 12px;font-size:13px;color:#777}
.signup span{background:var(--footer-bar);color:#fff;padding:6px 10px;border-radius:3px;font-size:13px}
.social{position:absolute;left:858px;top:225px;display:flex;gap:18px}
.social i{width:40px;height:40px;border-radius:50%;background:#5b646c}
.footer-bar{position:absolute;left:0;bottom:0;width:1200px;height:33px;background:var(--footer-bar);text-align:center;line-height:33px;font-size:12px}
</style>
</head>
<body>

<header class="site-header abs">
  <div class="util abs"><span>Register</span><span class="sep">/</span><span>Sign in</span>
    <div class="search">SEARCH KEYWORDS
      <svg width="18" height="18" viewBox="0 0 18 18"><circle cx="7" cy="7" r="5" fill="none" stroke="#1f3d5e" stroke-width="2.4"/><line x1="11" y1="11" x2="16" y2="16" stroke="#1f3d5e" stroke-width="3"/></svg>
    </div>
  </div>
  <div class="brand abs"><span class="mark"></span><span class="name">QuantoMesh</span></div>
  <div class="brand-tag abs">Algorithmic Trading Platform</div>
  <nav class="nav abs"><a>Home</a><a>About Us</a><a class="active">Services</a><a>Blog</a><a>Contact Us</a></nav>
</header>

<section class="hero abs">
  <h1>QuantoMesh Software</h1>
  <p>Lorem Ipsum is simply dummy text of the printing and typesetting industry. Lorem Ipsum has been the industry's standard dummy text ever since the 1500s, when an unknown printer took a galley of type and scrambled it to make a type specimen book. It has survived not only five centuries, but also</p>
  <div class="hero-art abs" role="img" aria-label="Illustration of business people standing before rising growth arrows"></div>
  <span class="btn btn-buy">Buy now</span>
  <span class="btn btn-demo">Get Demo</span>
  <div class="dots abs"><i></i><i class="on"></i><i></i></div>
</section>

<div class="dropdown abs">
  <a>Services</a><a>Services</a><a class="current">Services</a><a>Services</a><a>Services</a>
</div>

<section class="why">
  <h2>Why QuantoMesh software</h2>
  <p class="why-text abs">Lorem Ipsum is simply dummy text of the printing and typesetting industry. Lorem Ipsum has been the industry's standard dummy text ever since the 1500s, when an unknown printer took a galley of type and scrambled it to make a type specimen book. It has survived not only five centuries, but also the leap into electronic typesetting, remaining essentially unchanged. It was popularised in the 1960s with the release of Letraset sheets containing Lorem Ipsum passages, and more recently with desktop publishing software like</p>
  <ul class="benefits abs">
    <li><svg width="22" height="22" viewBox="0 0 22 22"><circle cx="11" cy="11" r="11" fill="#1f3d5e"/><path d="M8 6l8 5-8 5z" fill="#fff"/></svg>First benefit goes here</li>
    <li><svg width="22" height="22" viewBox="0 0 22 22"><circle cx="11" cy="11" r="11" fill="#1f3d5e"/><path d="M8 6l8 5-8 5z" fill="#fff"/></svg>Second benefit goes here</li>
    <li><svg width="22" height="22" viewBox="0 0 22 22"><circle cx="11" cy="11" r="11" fill="#1f3d5e"/><path d="M8 6l8 5-8 5z" fill="#fff"/></svg>Third benefit goes here</li>
    <li><svg width="22" height="22" viewBox="0 0 22 22"><circle cx="11" cy="11" r="11" fill="#1f3d5e"/><path d="M8 6l8 5-8 5z" fill="#fff"/></svg>Fourth benefit goes here</li>
  </ul>
  <div class="tablet abs"><div class="screen" role="img" aria-label="Screenshot of the trading app showing a spending chart and account figures"></div></div>
  <span class="btn-download abs">Download Demo</span>
</section>

<div class="rule abs" style="top:1280px"></div>

<section class="services">
  <h2>Avialable Services</h2>
  <div class="service abs" style="left:31px"><div class="disc on">
    <svg width="40" height="60" viewBox="0 0 40 60"><path d="M20 2a17 17 0 0 0-10 31c2 2 3 4 3 7h14c0-3 1-5 3-7A17 17 0 0 0 20 2z" fill="#222"/><rect x="13" y="43" width="14" height="5" fill="#222"/><rect x="15" y="50" width="10" height="5" rx="2" fill="#222"/></svg>
  </div><h3>Producr Feature</h3></div>
  <div class="service abs" style="left:338px"><div class="disc">
    <svg width="70" height="52" viewBox="0 0 70 52"><path d="M2 6h22l6 6h38v38H2z" fill="#1f3d5e"/><path d="M2 20h66v30H2z" fill="#2c5682"/></svg>
  </div><h3>Documentation<br>and Demo</h3></div>
  <div class="service abs" style="left:649px"><div class="disc">
    <svg width="60" height="50" viewBox="0 0 60 50"><rect x="2" y="8" width="56" height="40" rx="4" fill="#1f3d5e"/><rect x="22" y="2" width="16" height="10" rx="2" fill="#1f3d5e"/><circle cx="20" cy="24" r="6" fill="#fff"/><path d="M10 40a10 8 0 0 1 20 0z" fill="#fff"/><rect x="34" y="20" width="18" height="4" fill="#fff"/><rect x="34" y="30" width="14" height="4" fill="#fff"/></svg>
  </div><h3>Professional<br>Services</h3></div>
  <div class="service abs" style="left:961px"><div class="disc">
    <svg width="44" height="60" viewBox="0 0 44 60"><path d="M22 2c10 8 12 22 8 36H14C10 24 12 10 22 2z" fill="#1f3d5e"/><circle cx="22" cy="20" r="5" fill="#fff"/><path d="M14 30L4 44l10-2zM30 30l10 14-10-2z" fill="#1f3d5e"/><path d="M17 42h10l-5 14z" fill="#1f3d5e"/></svg>
  </div><h3>Training</h3></div>
  <p class="service-summary abs">"Lorem Ipsum is simply dummy text of the printing and typesetting industry. Lorem Ipsum has been the industry's standard dummy text ever since the 1500s, when an unknown printer took a galley of type and scrambled it to make a type specimen book. It has survived not only five centuries, but also the leap into electronic typesetting, remaining essentially unchanged. It was popularised in the 1960s with the release of Letraset sheets containing Lorem Ipsum passages, and more recently with desktop publishing software like Aldus PageMaker. Lorem Ipsum is simply dummy text of the printing and typesetting industry. Lorem Ipsum has been the industry's standard dummy text ever since the 1500s, when an unknown printer.</p>
  <span class="btn-dark abs" style="left:1080px;top:1790px;width:84px;height:32px;line-height:32px">Read more</span>
</section>

<div class="rule abs" style="top:1910px"></div>
<div class="col-rule abs"></div>

<h2 class="news-head abs">Latest News</h2>
<h2 class="testi-head abs">Testimonials</h2>
<div class="arrows abs"><i></i><i></i></div>

<article class="news-item abs" style="top:2060px"><div class="thumb" role="img" aria-label="Photo of a hand placing a coin beside a chart"></div><h4>Lorem Ipsum is simply dummy text of the</h4><time>May 6-2015</time><p>Lorem Ipsum is simply dummy text of the printing and typesetting industry. Lorem Ipsum has been the industry's standard dummy text ever since the</p><span class="more">Read more</span></article>
<article class="news-item abs" style="top:2260px"><div class="thumb" role="img" aria-label="Photo of a hand pointing at a growth chart"></div><h4>Lorem Ipsum is simply dummy text of the</h4><time>May 6-2015</time><p>Lorem Ipsum is simply dummy text of the printing and typesetting industry. Lorem Ipsum has been the industry's standard dummy text ever since the</p><span class="more">Read more</span></article>
<article class="news-item abs" style="top:2450px"><div class="thumb" role="img" aria-label="Photo of a hand placing a coin beside a chart"></div><h4>Lorem Ipsum is simply dummy text of the</h4><time>May 6-2015</time><p>Lorem Ipsum is simply dummy text of the printing and typesetting industry. Lorem Ipsum has been the industry's standard dummy text ever since the</p><span class="more">Read more</span></article>

<figure class="testimonial abs" style="top:2058px"><blockquote>"Lorem Ipsum is simply dummy text of the printing and typesetting industry. Lorem Ipsum has been the industry's standard dummy text ever since the 1500s, when an unknown printer took a galley of type and scrambled</blockquote><cite>Mr. Hollins (CEO of Cpmpany Name)</cite><div class="photo" role="img" aria-label="Customer portrait photo"></div></figure>
<figure class="testimonial abs" style="top:2245px"><blockquote>"Lorem Ipsum is simply dummy text of the printing and typesetting industry. Lorem Ipsum has been the industry's standard dummy text ever since the 1500s, when an unknown printer took a galley of type and scrambled</blockquote><cite>Mr. Hollins (CEO of Cpmpany Name)</cite><div class="photo" role="img" aria-label="Customer portrait photo"></div></figure>
<figure class="testimonial abs" style="top:2440px"><blockquote>"Lorem Ipsum is simply dummy text of the printing and typesetting industry. Lorem Ipsum has been the industry's standard dummy text ever since the 1500s, when an unknown printer took a galley of type and scrambled</blockquote><cite>Mr. Hollins (CEO of Cpmpany Name)</cite><div class="photo" role="img" aria-label="Customer portrait photo"></div></figure>

<footer class="site-footer abs">
  <h5 style="left:33px">Quick Links</h5>
  <ul class="quick"><li>Home</li><li>About Us</li><li>Services</li><li>Projects</li><li>Software</li><li>Clients</li><li>Site Map</li><li>Privacy Policy</li><li>Contact Us</li></ul>
  <h5 style="left:445px">Contact Us</h5>
  <div class="contact-row" style="top:95px"><svg width="16" height="22" viewBox="0 0 16 22"><path d="M8 0a8 8 0 0 0-8 8c0 6 8 14 8 14s8-8 8-14a8 8 0 0 0-8-8z" fill="#c7ccd0"/><circle cx="8" cy="8" r="3" fill="#3a4249"/></svg><span>27 Larkspur Street<br>Fairbrook , CA 90011<br>United State</span></div>
  <div class="contact-row" style="top:195px"><svg width="18" height="18" viewBox="0 0 18 18"><path d="M4 1l3 4-2 2c1 3 3 5 6 6l2-2 4 3-2 3C8 17 1 10 1 3z" fill="#c7ccd0"/></svg><span>+44 700 900 412</span></div>
  <div class="contact-row" style="top:235px"><svg width="18" height="14" viewBox="0 0 18 14"><rect width="18" height="14" fill="#c7ccd0"/><path d="M0 0l9 7 9-7" fill="none" stroke="#3a4249" stroke-width="1.5"/></svg><span>info@quantomesh-mail.example</span></div>
  <h5 style="left:858px">Get in Touchs</h5>
  <div class="news-label">Newsletter sign up</div>
  <div class="signup">Enter your email here<span>Sign up</span></div>
  <div class="social"><i></i><i></i><i></i><i></i></div>
  <div class="footer-bar">Copyright All right are Reserved by QuantoMesh.com</div>
</footer>

</body>
</html>
```